Need Business Card for our Real Estate Business with Sales Executive's Picture

PANTONE 484 C ( RED)

PANTONE 2766 C ( BLUE

Industry/Entity Type

Real Estate

Contact Information for Business Card

Name, Mobile, email, & picture of Person
Agency Phone, address, Web address

Requirements
Must have
• Our Logo Colours, Agent Picture,

```html
<!DOCTYPE html>
<html lang="en">
<head>
<meta charset="utf-8">
<title>Meridian Real Estate – Business Card</title>
<link rel="stylesheet" href="https://fonts.googleapis.com/css2?family=Open+Sans:wght@400;600&display=swap">
<style>
  :root {
    --backdrop: #c9ccd0;
    --card-white: #ffffff;
    --navy: #0a1838;
    --ink: #454545;
    --rule: #5a5a5a;
    --icon: #5c5c5c;
    --photo-top: #3a4f8c;
    --photo-bottom: #1f2e63;
  }
  * { margin: 0; padding: 0; box-sizing: border-box; }
  html, body {
    width: 1200px; height: 1000px; overflow: hidden;
    background: var(--backdrop);
    font-family: "Open Sans", Arial, sans-serif;
  }
  .canvas { position: relative; width: 1200px; height: 1000px; }

  .card {
    position: absolute;
    width: 681px; height: 388px;
    overflow: hidden;
    box-shadow: 14px 14px 18px rgba(0,0,0,0.22);
  }
  .card--front { left: 262px; top: 85px; background: var(--card-white); }
  .card--back  { left: 262px; top: 525px; background: var(--navy); }

  .card__swoosh, .card__wave { position: absolute; left: 0; top: 0; }

  .agent-photo {
    position: absolute; left: 35px; top: 33px;
    width: 124px; height: 177px;
    background: linear-gradient(180deg, var(--photo-top), var(--photo-bottom));
  }

  .brand-front {
    position: absolute; left: 244px; top: 75px; width: 200px;
    text-align: center; color: var(--navy);
    font-weight: 600; line-height: 1;
  }
  .brand-front__name { font-size: 22px; letter-spacing: 2px; }
  .brand-front__sub { font-size: 7px; letter-spacing: 1.5px; margin-top: 3px; }
  .brand-front__mark {
    display: block; width: 12px; height: 12px; margin: 0 auto 8px;
    background: var(--navy);
  }

  .agent-name {
    position: absolute; left: 189px; top: 138px;
    font-size: 24px; color: var(--ink);
  }
  .agent-role {
    position: absolute; left: 186px; top: 172px; width: 300px;
    text-align: center; font-size: 18px; color: var(--ink);
  }
  .divider {
    position: absolute; left: 27px; top: 209px;
    width: 565px; height: 1.5px; background: var(--rule);
  }
  .office-address {
    position: absolute; left: 202px; top: 220px;
    font-size: 19px; color: var(--ink);
  }
  .contact-list { position: absolute; left: 40px; top: 265px; list-style: none; }
  .contact-list li {
    display: flex; align-items: center; height: 31.5px;
    font-size: 17px; color: var(--ink);
  }
  .contact-list svg { width: 18px; height: 18px; margin-right: 15px; flex: none; }

  .brand-back {
    position: absolute; left: 190px; top: 150px; width: 300px;
    text-align: center; color: var(--card-white); font-weight: 400; line-height: 1;
  }
  .brand-back__mark {
    display: block; width: 22px; height: 22px; margin: 0 auto 14px;
    background: var(--card-white);
  }
  .brand-back__name { font-size: 44px; letter-spacing: 3px; }
  .brand-back__sub { font-size: 10px; letter-spacing: 3px; margin-top: 8px; }
</style>
</head>
<body>
<main class="canvas">

  <section class="card card--front" aria-label="Business card front">
    <svg class="card__swoosh" width="681" height="388" viewBox="0 0 681 388" aria-hidden="true">
      <path fill="var(--navy)" d="M513 0 L553 0 C590 60 630 130 618 185 C606 250 560 330 578 388 L510 388 C540 320 610 250 598 190 C588 130 540 50 513 0 Z"/>
    </svg>

    <div class="agent-photo" role="img" aria-label="Portrait photo of the sales executive in a navy suit"></div>

    <div class="brand-front">
      <span class="brand-front__mark"></span>
      <div class="brand-front__name">MERIDIAN</div>
      <div class="brand-front__sub">REAL ESTATE</div>
    </div>

    <p class="agent-name">Name of Sales Executive's</p>
    <p class="agent-role">Sales Executive</p>
    <div class="divider"></div>
    <p class="office-address">address of Meridian Real Estate</p>

    <ul class="contact-list">
      <li>
        <svg viewBox="0 0 18 18" aria-hidden="true"><circle cx="9" cy="9" r="7.5" fill="none" stroke="var(--icon)" stroke-width="1.4"/><path d="M6.3 5.2 L7.6 5 L8.3 6.9 L7.5 7.6 C8 8.8 9 9.9 10.3 10.5 L11 9.7 L12.9 10.4 L12.7 11.7 C10 12.3 5.8 8.2 6.3 5.2 Z" fill="var(--icon)"/></svg>
        mobile / agency phone
      </li>
      <li>
        <svg viewBox="0 0 18 18" aria-hidden="true"><rect x="1.5" y="4" width="15" height="10" fill="var(--icon)"/><path d="M1.5 4 L9 10 L16.5 4" fill="none" stroke="#fff" stroke-width="1.2"/></svg>
        meridian@email.com
      </li>
      <li>
        <svg viewBox="0 0 18 18" aria-hidden="true"><g fill="none" stroke="var(--icon)" stroke-width="1.3"><circle cx="9" cy="9" r="7.5"/><ellipse cx="9" cy="9" rx="3.2" ry="7.5"/><path d="M1.5 9 H16.5 M2.6 5.2 H15.4 M2.6 12.8 H15.4"/></g></svg>
        www.webaddress.com
      </li>
    </ul>
  </section>

  <section class="card card--back" aria-label="Business card back">
    <svg class="card__wave" width="681" height="388" viewBox="0 0 681 388" aria-hidden="true">
      <path fill="var(--card-white)" d="M0 183 C120 195 250 325 440 330 C560 332 620 200 681 183 L681 238 C610 262 560 345 440 345 C260 345 130 252 0 250 Z"/>
    </svg>

    <div class="brand-back">
      <span class="brand-back__mark"></span>
      <div class="brand-back__name">MERIDIAN</div>
      <div class="brand-back__sub">REAL ESTATE</div>
    </div>
  </section>

</main>
</body>
</html>
```